Industrial / automotive service company
Renewing and reconditioning solutions
Simple
Ted Pelkin
VP - Industrial Division
217 Marston Crescent NW
Calgary, Alberta
T2P 4G6
t-pelkin@zorvamail.com

```html
<!DOCTYPE html>
<html lang="en">
<head>
<meta charset="utf-8">
<title>Tovalmex Services Inc. – Business Card</title>
<link rel="stylesheet" href="https://fonts.googleapis.com/css2?family=Exo+2:wght@600&family=Open+Sans:wght@400;600&display=swap">
<style>
  :root {
    --bg: #e6e7e8;
    --green: #8cc63f;
    --white: #ffffff;
    --panel-grey: #a7a9ac;
    --logo-grey: #6d6e71;
    --text-light: #f4f4f4;
    --shadow: rgba(0, 0, 0, 0.18);
  }
  * { margin: 0; padding: 0; box-sizing: border-box; }
  html, body {
    width: 1200px; height: 838px; overflow: hidden;
    background: var(--bg);
    font-family: "Open Sans", Arial, sans-serif;
  }
  .stage {
    width: 1200px; height: 838px;
    display: flex; align-items: center; justify-content: center; gap: 60px;
  }
  .card {
    width: 525px; height: 300px; position: relative;
    box-shadow: 0 6px 18px var(--shadow);
    overflow: hidden;
  }
  /* Front */
  .card--front { background: var(--green); }
  .front-panel {
    position: absolute; left: 18px; top: 18px; bottom: 18px; right: 64px;
    background: var(--white); border-radius: 14px;
    display: flex; align-items: center; justify-content: center;
  }
  .brand {
    display: flex; align-items: center; gap: 12px;
    color: var(--logo-grey);
    font-family: "Exo 2", Arial, sans-serif; font-weight: 600;
  }
  .brand-dot { width: 22px; height: 22px; border-radius: 50%; background: var(--green); }
  .brand-name { font-size: 34px; line-height: 1.05; }
  .brand-name small { display: block; font-size: 17px; letter-spacing: 2px; }
  .front-role {
    position: absolute; right: 0; top: 0; bottom: 0; width: 64px;
    display: flex; align-items: center; justify-content: center;
  }
  .front-role span {
    transform: rotate(-90deg); white-space: nowrap;
    color: var(--white); font-size: 11px; letter-spacing: 1.5px;
  }
  /* Back */
  .card--back { background: var(--white); }
  .back-panel {
    position: absolute; left: 18px; top: 18px; right: 64px; bottom: 70px;
    background: var(--panel-grey); border-radius: 14px;
    display: flex; flex-direction: column; justify-content: flex-end;
    padding: 0 20px 16px;
  }
  .contact {
    display: flex; flex-wrap: wrap; gap: 4px 16px;
    color: var(--text-light); font-size: 9.5px; letter-spacing: 0.3px;
  }
  .contact-item { display: flex; align-items: center; gap: 5px; }
  .contact-item svg { width: 10px; height: 10px; fill: var(--text-light); }
</style>
</head>
<body>
<main class="stage">
  <section class="card card--front">
    <div class="front-panel">
      <div class="brand">
        <span class="brand-dot"></span>
        <span class="brand-name">Tovalmex<small>Services Inc.</small></span>
      </div>
    </div>
    <div class="front-role"><span>Ted Pelkin &nbsp;|&nbsp; VP - Industrial Division</span></div>
  </section>

  <section class="card card--back">
    <div class="back-panel">
      <div class="contact">
        <span class="contact-item">
          <svg viewBox="0 0 10 10"><path d="M5 0a3.5 3.5 0 0 0-3.5 3.5C1.5 6 5 10 5 10s3.5-4 3.5-6.5A3.5 3.5 0 0 0 5 0zm0 5a1.5 1.5 0 1 1 0-3 1.5 1.5 0 0 1 0 3z"/></svg>
          217 Marston Crescent NW, Calgary, Alberta T2P 4G6
        </span>
        <span class="contact-item">
          <svg viewBox="0 0 10 10"><path d="M2 0.5l2 2-1 1.2c.6 1.3 1.6 2.3 2.9 2.9L7 5.6l2 2-1.2 1.6C4.6 9 1 5.4.8 2.2z"/></svg>
          (403) 555-0182
        </span>
        <span class="contact-item">
          <svg viewBox="0 0 10 10"><path d="M0 2h10v6H0zM0 2l5 3.5L10 2" stroke="#a7a9ac" stroke-width="0.8"/></svg>
          t-pelkin@zorvamail.com
        </span>
        <span class="contact-item">
          <svg viewBox="0 0 10 10"><circle cx="5" cy="5" r="4.5"/></svg>
          www.tovalmex.com
        </span>
      </div>
    </div>
  </section>
</main>
</body>
</html>
```